Startup photography business has a new logo, now we need business cards

Design a business card for the two partners of our business.
Our business Brisk Pelican has a new logo and we need to design a business card to showcase it and us.
Our colours of blue and orange are punchy and vivid, but how can we make the most of it on our card?

It should have our name Brisk Pelican
name of partner
phone number
email
website

Industry/Entity Type

Professional Photography

Contact Information for Business Card

Tom Ashworth
+61 400 55 61 72
tom@briskpelican.com.au
briskpelican.com.au

second card
Neil Porter
+61 400 918 263
neil@briskpelican.com.au
briskpelican.com.au

Colors
f37122
f68d4c
33a6d7
0592cd

Requirements
Must have
• one version of our logo, we have included options
• Name
• phone number
• email
• website
Nice to have
• instagram briskpelicanmedia
• twitter briskpelicanmedia
• facebook briskpelicanmedia

```html
<!DOCTYPE html>
<html lang="en">
<head>
<meta charset="utf-8">
<title>Brisk Pelican – Business Cards</title>
<link rel="stylesheet" href="https://fonts.googleapis.com/css2?family=Source+Sans+3:wght@400;600;700&display=swap">
<style>
  :root {
    --orange: #f37122;
    --orange-soft: #f68d4c;
    --blue: #33a6d7;
    --blue-deep: #0592cd;
    --sky: #17b9ee;
    --white: #ffffff;
    --backdrop: #ecebe8;
  }
  * { box-sizing: border-box; margin: 0; padding: 0; }
  html, body {
    width: 1200px; height: 900px; overflow: hidden;
    background: var(--backdrop);
    font-family: "Source Sans 3", "Myriad Pro", Arial, sans-serif;
  }
  .canvas { position: relative; width: 1200px; height: 900px; }
  .card {
    position: absolute; overflow: hidden;
    background: var(--white);
    box-shadow: 0 6px 18px rgba(0,0,0,0.18);
  }
  .card-front { left: 78px; top: 34px; width: 588px; height: 364px; }
  .card-back  { left: 388px; top: 505px; width: 566px; height: 352px; }
  .card-shapes { position: absolute; inset: 0; }
  .brand-name {
    position: absolute; color: var(--white);
    font-weight: 700; letter-spacing: 0.5px; white-space: nowrap;
  }
  .card-front .brand-name { left: 30px; top: 46px; font-size: 36px; }
  .person-name {
    position: absolute; left: 30px; top: 188px;
    color: var(--white); font-size: 21px; font-weight: 600;
  }
  .contact-list {
    position: absolute; left: 30px; top: 255px; list-style: none;
    color: var(--white); font-size: 16px; line-height: 25px;
  }
  .contact-list li { display: flex; align-items: center; gap: 8px; }
  .contact-list svg { width: 12px; height: 12px; flex: none; }
  .back-brand {
    position: absolute; left: 296px; top: 268px;
    display: flex; align-items: center; gap: 12px;
  }
  .back-brand .brand-dot {
    width: 22px; height: 22px; border-radius: 50%; background: var(--white);
  }
  .back-brand .brand-name { position: static; font-size: 32px; }
</style>
</head>
<body>
<main class="canvas">

  <section class="card card-front">
    <svg class="card-shapes" viewBox="0 0 588 364" width="588" height="364">
      <defs>
        <radialGradient id="blueMascot" cx="50%" cy="45%" r="60%">
          <stop offset="0%" stop-color="#7fd3f3"/>
          <stop offset="100%" stop-color="#17b9ee"/>
        </radialGradient>
      </defs>
      <path d="M0 0 H400 C320 60 285 170 310 260 C320 310 340 345 350 364 H0 Z" fill="var(--orange)"/>
      <ellipse cx="450" cy="185" rx="150" ry="172" fill="url(#blueMascot)"
               role="img" aria-label="Brand mascot illustration in blue"/>
    </svg>
    <div class="brand-name">Brisk Pelican</div>
    <div class="person-name">Tom Ashworth</div>
    <ul class="contact-list">
      <li>
        <svg viewBox="0 0 12 12"><path d="M2.5 0.5 L4.5 0.5 L5 3.2 L3.7 4.2 C4.4 5.8 6.2 7.6 7.8 8.3 L8.8 7 L11.5 7.5 L11.5 9.5 C11.5 10.6 10.6 11.5 9.5 11.5 C4.5 11.2 0.8 7.5 0.5 2.5 C0.5 1.4 1.4 0.5 2.5 0.5 Z" fill="#fff"/></svg>
        +61 400 55 61 72
      </li>
      <li>
        <svg viewBox="0 0 12 12"><rect x="0.5" y="2" width="11" height="8" fill="#fff"/><path d="M0.5 2 L6 6.5 L11.5 2" fill="none" stroke="var(--orange)" stroke-width="1"/></svg>
        tom@briskpelican.com.au
      </li>
      <li>
        <svg viewBox="0 0 12 12"><circle cx="6" cy="6" r="5.5" fill="#fff"/><path d="M0.5 6 H11.5 M6 0.5 C3.5 3.5 3.5 8.5 6 11.5 M6 0.5 C8.5 3.5 8.5 8.5 6 11.5" fill="none" stroke="var(--orange)" stroke-width="0.8"/></svg>
        briskpelican.com.au
      </li>
    </ul>
  </section>

  <section class="card card-back">
    <svg class="card-shapes" viewBox="0 0 566 352" width="566" height="352">
      <defs>
        <radialGradient id="orangeMascot" cx="50%" cy="45%" r="60%">
          <stop offset="0%" stop-color="#f68d4c"/>
          <stop offset="100%" stop-color="#f37122"/>
        </radialGradient>
      </defs>
      <ellipse cx="105" cy="185" rx="150" ry="172" fill="url(#orangeMascot)"
               role="img" aria-label="Brand mascot illustration in orange"/>
      <path d="M180 0 H566 V352 H200 C255 290 275 180 240 100 C220 50 200 20 180 0 Z" fill="var(--sky)"/>
    </svg>
    <div class="back-brand">
      <span class="brand-dot"></span>
      <span class="brand-name">Brisk Pelican</span>
    </div>
  </section>

</main>
</body>
</html>
```